Organic - Eco Friendly Coconut Bowls - Mavu Dishes Catalogue

We want a brand new catalogue for our company . This catalogue needs to be clean , easy to read . We are a organic coconut bowl company . Our catalogue must be environmental , coconuty , palm trees , clean , organic , sustainable and eco friendly type catalogue . We are looking to give the best and more clear information about our bowls to our customers. In attached our old catalogue we need something brand new and totally different. We want greeny , some palm trees would be nice , or even the palm leaves

Important to add on the catalogue
Swedish owned company - Largest Scandinavian Producer and Supplier of Coconut Bowls
Each bowl has a diameter of 12-14cm (4.7-5.5 inches)
Average depth of 6cm (2.3 inches)
Approximate volume of 450mL (15.2 fl.oz.)

We have image and prices of each one single bowl , fork and spoon .

Base our information given on the old catalogue and complement on the new catalogue , do a bit of research about the thema aswell .

Bowls must all come in Price order from 99kr to 129kr

We now have added price for 15 bowls aswell

15 bowls 99kr - 975kr - 97 euros
15 bowls 119kr - 1125kr -
15 bowls 129 kr - 1200kr

Please add Denmark , Sweden , Norway , Finland and Iceland flags

Add vectors of - Plant Based , Organic , Sustainable , Vegan , Cruently Free , Handcrafted ( check online for those to have an idea)

Bowls must all come in Price order from 99kr to 129kr We now have added price for 15 bowls aswell ONLY FOR THE REGULAR BOWLS , NOT MINI BOWLS 15 bowls 99kr - 975kr - 95 euros 15 bowls 119kr - 1125kr - 110 euros 15 bowls 129 kr - 1200kr - 118 euros Please add Denmark , Sweden , Norway , Finland and Iceland flags Add vectors of - Plant Based , Organic , Sustainable , Vegan , Cruently Free , Handcrafted ( check online for those to have an idea)

https://www.tarevanhome.com.au/ we love this guys ,style , fonts and color mix would check them out for inspiration

Target Market(s)

Organic Stores worldwide , customers interested in ecologic , eco-friendly , sustainable products

Industry/Entity Type

It Company

Colors

Designer to choose colors to be used in the design.

Requirements
Must have
• All information from the old catalogue on it , prices , information and all image of products and our logo . Also add the information
• Swedish owned company - Largest Scandinavian Producer and Supplier of Coconut Bowls
• Each bowl has a diameter of 12-14cm (4.7-5.5 inches)
• Average depth of 6cm (2.3 inches)
• Approximate volume of 450mL (15.2 fl.oz.)
• We just want be sure that the customers have a good idea of the plantbased , vegan , vegetarian , organic , sustainable community. Also add to the catalogue that our product is 100% Vegan , we use coconut virgin oil to polish , all bowls are handcrafted by local artisans.
• Important to make notes that is ecological friendly , its sustainable ,
• Our CARE TIPS PAGE MUST HAVE THE BELOW INFO
• CARE
• -
• Caring for coconut shell bowls is important as they are 100%
• natural products. By following these basic care instructions, customers will enjoy long-lasting coconut bowls.
• WASHING
• -
• Hand wash with lukewarm, soapy water. Do not use in the
• dishwasher or soak for a long period.
• EATING
• -
• Coconut bowls are best suited to room temperature and cool foods. For warmer foods (to ensure durability), prepare the bowl for the change in temperature by first rinsing your bowl in
• lukewarm water and set aside until dry.
• On rare occasions, hot foods can cause the bowls to crack.
• USING
• -
• Do not expose coconut bowls to extreme heat, and do not use in the refrigerator, microwave, oven, or dishwasher.
• TIPS
• -
• Polish with virgin coconut oil (or an oil of your choice) every 10 or so uses to restore the coconut bowls smooth and shiny surface while resealing its pores.
• Because coconut bowls are a product of nature, their durability cannot always be predicted.
• OPEN THE OLD CATALOGUE IN ATTACHED TO SEE THE BOWLS PRICES !!! DONT FORGET PLEASE
Nice to have

```html
<!DOCTYPE html>
<html lang="en">
<head>
<meta charset="utf-8">
<title>Mavu Dishes – Wholesale Catalogue 2018</title>
<link rel="stylesheet" href="https://fonts.googleapis.com/css2?family=Lato:wght@400;700&family=Old+Standard+TT&display=swap">
<style>
  :root {
    --artboard: #76777b;
    --leaf-green: #17ad62;
    --leaf-deep: #0f9a52;
    --palm-dark: #2f6d12;
    --palm-mid: #5c9a24;
    --palm-light: #8fc046;
    --band-start: #1fae62;
    --band-end: #a4b93e;
    --title-yellow: #fff200;
    --accent-orange: #e87a2c;
    --vegan-green: #a6cf5d;
    --paper: #ffffff;
  }
  * { margin: 0; padding: 0; box-sizing: border-box; }
  html, body { width: 1200px; height: 576px; overflow: hidden; }
  body {
    position: relative;
    background: var(--artboard);
    font-family: "Lato", Arial, sans-serif;
  }
  .spread { position: absolute; left: 136px; top: 56px; width: 927px; height: 463px; display: flex; }

  /* Care tips page */
  .care-page {
    position: relative; width: 464px; height: 463px;
    background: linear-gradient(180deg, var(--leaf-green) 0%, #19ab60 55%, var(--leaf-deep) 100%);
    overflow: hidden; color: var(--paper);
  }
  .care-page__palms {
    position: absolute; left: 0; right: 0; bottom: 0; height: 240px;
    background: radial-gradient(ellipse at 30% 60%, rgba(120,210,150,.28), transparent 60%),
                radial-gradient(ellipse at 75% 40%, rgba(120,210,150,.18), transparent 55%);
  }
  .care-box {
    position: absolute; left: 62px; top: 66px; width: 340px; height: 274px;
    border: 4px solid rgba(255,255,255,.35);
    text-align: center; padding: 20px 22px 0;
  }
  .care-box__title {
    font-family: "Old Standard TT", Georgia, serif; font-weight: 400;
    font-size: 19px; letter-spacing: .5px; line-height: 1;
  }
  .care-box__rule { width: 190px; height: 1px; background: rgba(255,255,255,.8); margin: 8px auto 12px; }
  .care-box p { font-size: 7.3px; line-height: 1.35; margin-bottom: 9px; }
  .care-box p strong { display: block; font-weight: 700; }
  .care-box p.tight { margin-bottom: 0; }

  .follow {
    position: absolute; left: 0; right: 0; top: 410px;
    display: flex; justify-content: center; align-items: center; gap: 8px;
    font-size: 8px; font-weight: 700;
  }
  .follow__dot { width: 17px; height: 17px; border-radius: 50%; background: var(--paper); }
  .care-page__web { position: absolute; left: 0; right: 0; top: 437px; text-align: center; font-size: 6.5px; }

  /* Cover page */
  .cover-page { position: relative; width: 463px; height: 463px; background: var(--paper); overflow: hidden; }
  .palm-leaf { position: absolute; }
  .palm-leaf--left {
    left: 0; top: 0; width: 240px; height: 200px;
    background: radial-gradient(ellipse at 35% 30%, var(--palm-mid) 0%, var(--palm-dark) 40%, rgba(255,255,255,0) 72%);
  }
  .palm-leaf--top {
    left: 240px; top: 0; width: 130px; height: 160px;
    background: radial-gradient(ellipse at 50% 30%, var(--palm-light) 0%, var(--palm-mid) 35%, rgba(255,255,255,0) 70%);
  }
  .palm-leaf--right {
    left: 315px; top: 60px; width: 160px; height: 300px;
    background: radial-gradient(ellipse at 75% 55%, var(--palm-mid) 0%, var(--palm-dark) 35%, rgba(255,255,255,0) 70%);
  }
  .brand-mark {
    position: absolute; right: 15px; top: 24px;
    font-family: "Lato", Arial, sans-serif; font-weight: 700; font-size: 11px;
    letter-spacing: .5px; color: #1d1d1d;
  }
  .title-band {
    position: absolute; left: 0; top: 214px; width: 312px; height: 79px;
    background: linear-gradient(90deg, var(--band-start) 0%, #6cc08a 45%, var(--band-end) 100%);
    text-align: center; padding-top: 14px;
  }
  .title-band__name {
    font-family: "Old Standard TT", Georgia, serif; font-weight: 400;
    font-size: 31px; line-height: 1; color: var(--title-yellow);
  }
  .title-band__sub {
    margin-top: 8px; display: flex; justify-content: center; align-items: center; gap: 6px;
    font-size: 10px; letter-spacing: 2px; color: var(--paper);
  }
  .title-band__sub::before, .title-band__sub::after { content: ""; width: 22px; height: 1px; background: var(--paper); }

  .facts { position: absolute; left: 40px; top: 314px; list-style: none; }
  .facts li {
    position: relative; padding-left: 14px; margin-bottom: 3px;
    font-size: 11px; line-height: 1.15; color: var(--accent-orange);
  }
  .facts li::before {
    content: ""; position: absolute; left: 0; top: 4px;
    width: 6px; height: 6px; border-radius: 50%; background: var(--accent-orange);
  }
  .vegan-tag {
    position: absolute; left: 378px; top: 432px; width: 68px; height: 20px;
    border: 2px solid var(--vegan-green); outline: 1px solid var(--vegan-green); outline-offset: 1px;
    background: #d9ebb9; color: var(--vegan-green);
    font-size: 8px; font-weight: 700; display: flex; align-items: center; justify-content: center;
  }
</style>
</head>
<body>
  <main class="spread">
    <section class="care-page">
      <div class="care-page__palms" role="img" aria-label="Faint palm tree silhouettes"></div>
      <div class="care-box">
        <h2 class="care-box__title">CARE TIPS</h2>
        <div class="care-box__rule"></div>
        <p><strong>Washing:</strong>Do not use dishwasher or soak for a long period</p>
        <p>Caring for coconut shell bowl is important as they are 100% natural products. By following these basic care instructions, customers will enjoy long-lasting coconut bowls.</p>
        <p>Coconut bowls are best suited to room temperature and cool foods. For warmer foods (to ensure durability), prepare the bowl for the change in temperature by first rinsing your bowl in lukewarm water and set aside until dry. On rare occasions, hot foods can cause the bowls to crack.</p>
        <p>Do not expose coconut bowls to extreme heat, and do not use in the refrigerator, microwave, oven, or dishwasher.</p>
        <p class="tight"><strong>Longer Lasting Bowls:</strong>Polish with virgin coconut oil (or an oil of your choice) every 10 or so uses to restore the coconut bowls smooth and shiny surface while resealing its pores. Because coconut bowls are a product of nature, their durability cannot always be predicted.</p>
      </div>
      <div class="follow">
        <span>Follow us on:</span>
        <span class="follow__dot"></span>
        <span class="follow__dot"></span>
      </div>
      <div class="care-page__web">www.mavudishes.se | www.lotusplates.se</div>
    </section>

    <section class="cover-page">
      <div class="palm-leaf palm-leaf--left" role="img" aria-label="Palm leaves reaching in from the top left"></div>
      <div class="palm-leaf palm-leaf--top" role="img" aria-label="Palm leaf hanging from the top"></div>
      <div class="palm-leaf palm-leaf--right" role="img" aria-label="Palm leaves along the right edge"></div>
      <div class="brand-mark">MAVU DISHES</div>
      <div class="title-band">
        <h1 class="title-band__name">MAVU DISHES</h1>
        <div class="title-band__sub">WHOLESALE CATALOGUE 2018</div>
      </div>
      <ul class="facts">
        <li>Swedish owned company</li>
        <li>Largest Scandinavian Producer<br>and Supplier of Coconut Bowls</li>
        <li>Each bowl has a diameter of 12-14 cm (4.7-5.5 inches)</li>
        <li>Average depth of 6 cm (2.3 inches)</li>
        <li>Approximate volume of 450mL (15.2 fl.oz.)</li>
      </ul>
      <div class="vegan-tag">100% VEGAN</div>
    </section>
  </main>
</body>
</html>
```